Never Stay Meek needs a book cover design

I need a book cover design for the following title:
Never Stay Meek-Grow a Bold Captain
Family methods from Cradle to Silver Years
by Dr. Walter P. Ondrak
I am interviewing a number of strong Canadian Leaders-specifically with regard to their experience of being parented. The book is a reaction today of parents having no backbone, no will nor ability to discipline their children. Many parents want to make a change but don't know how to.
Updates
Title should be "Never Stay Meek-Grow a Bold Captain" the rest is correct Added Wednesday, November 11, 2015
Here is an example of what we would need on the back cover in text only.
What does it take to raise a strong leader? Psychologist Dr. Walter P. Ondrak provides you with 6 must do strategies based on his 26 years of clinical experience and the interview of 6 strong leaders for this book. Strategies that you can start using today to insure your child’s success.
Target Market(s)
parents and grandparents
Requirements
Must have
- a way to communicate strength in parenting

```html
<!DOCTYPE html>
<html lang="en">
<head>
<meta charset="utf-8">
<title>Never Stay Meek-Grow a Bold Captain — Cover Spread</title>
<link rel="stylesheet" href="https://fonts.googleapis.com/css2?family=Pathway+Gothic+One&display=swap">
<style>
  :root {
    --paper-light: #f4f8f8;
    --paper-edge: #c3d7da;
    --blue-top: #0a8fd0;
    --blue-bottom: #0a4c7c;
    --ink-blue: #0c4f80;
    --white: #ffffff;
    --fold-line: #8aa0a6;
    --stage-center: #0d6497;
    --stage-edge: #073457;
  }
  * { margin: 0; padding: 0; box-sizing: border-box; }
  html, body { width: 941px; height: 1200px; overflow: hidden; }
  body {
    position: relative;
    font-family: "Pathway Gothic One", "Arial Narrow", sans-serif;
    font-weight: 400;
    background: radial-gradient(ellipse at 50% 60%, var(--stage-center), var(--stage-edge));
  }
  .cover-spread {
    position: absolute; left: 0; top: 0;
    width: 941px; height: 585px;
    background: radial-gradient(ellipse at 38% 45%, var(--paper-light) 0%, #e3eded 40%, var(--paper-edge) 100%);
    border-bottom: 1px solid var(--fold-line);
  }
  .back-cover { position: absolute; left: 0; top: 0; width: 415px; height: 585px; }
  .spine {
    position: absolute; left: 415px; top: 0; width: 111px; height: 585px;
    border-left: 1px solid var(--fold-line);
    border-right: 1px solid var(--fold-line);
  }
  .spine-author {
    position: absolute; top: 24px; left: 0; width: 100%;
    text-align: center; font-size: 13px; color: var(--ink-blue);
  }
  .spine-title {
    position: absolute; left: 55px; top: 86px;
    transform-origin: 0 0; transform: rotate(90deg) translateY(-50%);
    white-space: nowrap; font-size: 30px; color: var(--ink-blue);
    line-height: 1;
  }

  /* Front cover (used in the spread and as the flat showcase) */
  .front-cover { position: absolute; width: 415px; height: 585px; overflow: hidden; }
  .spread-front { left: 526px; top: 0; }
  .front-panel { position: absolute; left: 0; top: 0; width: 415px; height: 585px; }
  .portrait-area {
    position: absolute; left: 121px; top: 40px; width: 170px; height: 196px;
    border-radius: 80px 80px 18px 18px;
    background: linear-gradient(180deg, #f7fbfd, #e2eef5);
  }
  .front-title {
    position: absolute; left: 0; top: 262px; width: 415px;
    text-align: center; color: var(--white); font-weight: 400;
  }
  .front-title .line-lead { display: block; font-size: 66px; line-height: 72px; }
  .front-title .line-rest { display: block; font-size: 48px; line-height: 55px; }
  .front-author {
    position: absolute; left: 0; top: 537px; width: 415px;
    text-align: center; font-size: 18px; color: var(--ink-blue);
  }

  .showcase {
    position: absolute; left: 0; top: 586px; width: 941px; height: 614px;
  }
  .showcase-front {
    left: 300px; top: 62px;
    transform: scale(0.82); transform-origin: 0 0;
    background: linear-gradient(160deg, var(--paper-light), var(--paper-edge));
    box-shadow: 0 18px 40px rgba(0, 20, 40, 0.45);
  }
</style>
</head>
<body>
  <section class="cover-spread">
    <div class="back-cover"></div>

    <div class="spine">
      <p class="spine-author">Dr. Walter P. Ondrak</p>
      <p class="spine-title">Never Stay Meek-Grow a Bold Captain</p>
    </div>

    <div class="front-cover spread-front">
      <svg class="front-panel" viewBox="0 0 415 585" width="415" height="585">
        <defs>
          <linearGradient id="panelBlue" x1="0" y1="0" x2="0" y2="1">
            <stop offset="0" stop-color="#0a8fd0"/>
            <stop offset="1" stop-color="#0a4c7c"/>
          </linearGradient>
        </defs>
        <path fill="url(#panelBlue)"
              d="M2 0 L80 445 Q92 510 150 510 L265 510 Q323 510 340 455 L440 0 Z"/>
        <path fill="url(#panelBlue)" stroke="#dbe8ec" stroke-width="2.5"
              d="M14 -2 L89 440 Q100 492 152 492 L263 492 Q313 492 327 450 L425 -2 Z"/>
      </svg>
      <div class="portrait-area" role="img" aria-label="Line illustration of a confident young man in suit and tie"></div>
      <h1 class="front-title">
        <span class="line-lead">Never Stay</span>
        <span class="line-rest">Meek-Grow a</span>
        <span class="line-rest">Bold Captain</span>
      </h1>
      <p class="front-author">Dr. Walter P. Ondrak</p>
    </div>
  </section>

  <section class="showcase">
    <div class="front-cover showcase-front">
      <svg class="front-panel" viewBox="0 0 415 585" width="415" height="585">
        <defs>
          <linearGradient id="panelBlueShowcase" x1="0" y1="0" x2="0" y2="1">
            <stop offset="0" stop-color="#0a8fd0"/>
            <stop offset="1" stop-color="#0a4c7c"/>
          </linearGradient>
        </defs>
        <path fill="url(#panelBlueShowcase)"
              d="M2 0 L80 445 Q92 510 150 510 L265 510 Q323 510 340 455 L440 0 Z"/>
        <path fill="url(#panelBlueShowcase)" stroke="#dbe8ec" stroke-width="2.5"
              d="M14 -2 L89 440 Q100 492 152 492 L263 492 Q313 492 327 450 L425 -2 Z"/>
      </svg>
      <div class="portrait-area" role="img" aria-label="Line illustration of a confident young man in suit and tie"></div>
      <p class="front-title">
        <span class="line-lead">Never Stay</span>
        <span class="line-rest">Meek-Grow a</span>
        <span class="line-rest">Bold Captain</span>
      </p>
      <p class="front-author">Dr. Walter P. Ondrak</p>
    </div>
  </section>
</body>
</html>
```